Harbourline Refrigeration business card design

We would like a new design for our business card as we have a new logo.
We need generic business card to give our customers with our office details - with the option of making it individualized for each manager

Target Market(s)

Companies and homeowners

Industry/Entity Type

Air Conditioning

Contact Information for Business Card

We are not sure if we want single or double sided it will depend on the design we choose

Colors
33a6d7
0255a3

Requirements
Must have
• Logo
• phone: (08) 8721 5940
• email: harbourserve@tealnet.example
• website: www.harbourlinerefrigeration.example
• AU61420
• BLD472913
Nice to have
• Address - Shed 5/284 Tallis Rd, Port Ellery SA 5690

```html
<!DOCTYPE html>
<html lang="en">
<head>
<meta charset="utf-8">
<title>Harbourline Refrigeration – Business Card</title>
<link rel="stylesheet" href="https://fonts.googleapis.com/css2?family=Open+Sans:wght@400;600;700&display=swap">
<style>
  :root {
    --bg: #e9e9ea;
    --card: #141416;
    --card-edge: #1d1d20;
    --brand-light: #33a6d7;
    --brand-dark: #0255a3;
    --silver: #b9b9bd;
    --text: #f2f2f2;
    --rule: #e8e8ea;
  }
  * { box-sizing: border-box; margin: 0; padding: 0; }
  html, body {
    width: 1200px; height: 864px; overflow: hidden;
    background: var(--bg);
    font-family: "Open Sans", Arial, sans-serif;
  }
  .sheet {
    position: relative; width: 1200px; height: 864px;
    display: flex; align-items: center; justify-content: center; gap: 30px;
  }
  .card {
    position: relative; width: 550px; height: 314px; flex: none;
    background: linear-gradient(160deg, var(--card-edge), var(--card));
    border-radius: 4px;
    box-shadow: 0 10px 28px rgba(0,0,0,.25);
    color: var(--text);
    overflow: hidden;
  }
  /* Back side */
  .card-back { display: flex; flex-direction: column; align-items: center; justify-content: center; gap: 30px; }
  .back-brand { display: flex; align-items: center; gap: 14px; }
  .back-dot { width: 44px; height: 44px; border-radius: 50%;
    background: radial-gradient(circle at 35% 30%, #d8d8dc, #7a7a80); }
  .back-name { font-size: 26px; font-weight: 600; color: var(--silver); }
  .back-url { font-size: 13px; letter-spacing: 2px; color: var(--silver); }
  /* Front side */
  .card-front { display: flex; align-items: center; padding: 0 24px 0 30px; }
  .brand { flex: none; width: 190px; display: flex; align-items: center; gap: 10px; }
  .brand-dot { flex: none; width: 30px; height: 30px; border-radius: 50%; background: var(--brand-light); }
  .brand-name { font-size: 21px; font-weight: 700; line-height: 1.1; color: var(--brand-dark); }
  .divider { flex: none; width: 2px; height: 190px; margin: 0 18px;
    background: linear-gradient(to bottom, rgba(232,232,234,0), var(--rule) 50%, rgba(232,232,234,0)); }
  .details { flex: 1; min-width: 0; font-size: 13.5px; line-height: 1.4; }
  .person-name { font-size: 19px; font-weight: 700; color: var(--brand-dark); line-height: 1.1; }
  .person-role { font-size: 14px; font-weight: 600; color: var(--brand-light); margin-bottom: 6px; }
  .contact { list-style: none; margin-top: 4px; }
  .contact li { display: flex; align-items: center; gap: 7px; white-space: nowrap; }
  .contact svg { width: 12px; height: 12px; flex: none; fill: var(--brand-light); }
</style>
</head>
<body>
<main class="sheet">
  <section class="card card-back" aria-label="Card back">
    <div class="back-brand">
      <span class="back-dot"></span>
      <span class="back-name">Harbourline Refrigeration</span>
    </div>
    <p class="back-url">www.harbourlinerefrigeration.example</p>
  </section>

  <section class="card card-front" aria-label="Card front">
    <div class="brand">
      <span class="brand-dot"></span>
      <span class="brand-name">Harbourline Refrigeration</span>
    </div>
    <div class="divider"></div>
    <div class="details">
      <p class="person-name">MARCUS HALE</p>
      <p class="person-role">PRESIDENT</p>
      <p class="address">Shed 5/284 Tallis Rd<br>Port Ellery SA 5690<br>AU61420 | BLD472913</p>
      <ul class="contact">
        <li><svg viewBox="0 0 24 24"><path d="M6.6 10.8a15 15 0 0 0 6.6 6.6l2.2-2.2a1 1 0 0 1 1-.25 11.4 11.4 0 0 0 3.6.57 1 1 0 0 1 1 1V20a1 1 0 0 1-1 1A17 17 0 0 1 3 4a1 1 0 0 1 1-1h3.5a1 1 0 0 1 1 1c0 1.250.2 2.45.57 3.57a1 1 0 0 1-.25 1z"/></svg>(08) 8721 5940</li>
        <li><svg viewBox="0 0 24 24"><path d="M2 5h20v14H2z M2 5l10 8 10-8" fill="none" stroke="#33a6d7" stroke-width="2"/></svg>harbourserve@tealnet.example</li>
        <li><svg viewBox="0 0 24 24"><circle cx="12" cy="12" r="10" fill="none" stroke="#33a6d7" stroke-width="2"/><path d="M2 12h20M12 2c3 3 3 17 0 20M12 2c-3 3-3 17 0 20" fill="none" stroke="#33a6d7" stroke-width="1.6"/></svg>harbourlinerefrigeration.example</li>
      </ul>
    </div>
  </section>
</main>
</body>
</html>
```